Dr. Lumora needs a design for its website!

*Only need the design, coding is not required.
*Need desktop version ($500) and mobile/tablet version ($200)
*The attached files are not the exact layout we want, they are just for you to know what information should be included in those pages.
*The function of our website is like www.qavlo.hk
*For the background picture, prefer a lively picture and chinese people in it, NOT necessarily need a doctor or sick person in the picture

***Don't just copy the layout from the attachments or from the reference website, we are looking for creative ideas, non-ordinary designs!!!****

We are developing a website for the public to search a doctor by different criteria. At the initial stage, we need 4 pages to start with and other pages at later stage. I have attached the general idea of these pages but not necessarily to be exactly the same, I am looking for some new ideas.

This website needs a professional, modern, simple and user friendly design. The main color to be used in the website will be same as the color (R:0 G:139 B:205) used in our logo (see attached). We don't have any particular thoughts for the other color and the font to be used in the website. Can try to use circle outline for the icon in the navigation bar.

1. Home: will include 4 sections (see attached)

2. Doctor's details (see attached)

3. Health information: will include a short descriptions of this Health Info page and 5 sections (see attached)

4. News (see attached)

Reason: Not too many suitable designs to choose from and need more time to go through the designs

All

Medical

4 page

• must not be same as or looks too much like www.qavlo.hk
• prefer not to use black and red color

```html
<!DOCTYPE html>
<html lang="en">
<head>
<meta charset="utf-8">
<title>Dr. Lumora – Find a Doctor</title>
<link href="https://fonts.googleapis.com/css2?family=Open+Sans:wght@400;600;700;800&display=swap" rel="stylesheet">
<style>
:root{
  --page:#f2f2f2;
  --band:#e3e3e3;
  --brand:#1e5fd8;
  --brand-light:#0fa3ea;
  --panel:#2b6ff0;
  --panel-dark:#2c5cc5;
  --btn-dark:#153b9e;
  --navy:#123d9c;
  --teal:#6ee3dc;
  --teal-strong:#3fd0c8;
  --ink:#222;
  --muted:#8a8f99;
  --line:#d9d9d9;
  --white:#fff;
  --error:#e8434b;
}
*{box-sizing:border-box;margin:0;padding:0}
html,body{width:1200px;height:1200px;overflow:hidden}
body{background:var(--page);font-family:"Open Sans",sans-serif;color:var(--ink);position:relative}
.abs{position:absolute}
.top-band{left:0;top:0;width:1200px;height:597px;background:var(--band)}
.hero{left:119px;top:0;width:960px;height:519px;background:linear-gradient(120deg,#9aa3ab 0%,#c9cdd1 35%,#e8eaec 55%,#b4bbc2 80%,#8d97a0 100%)}
.lang{left:178px;top:0;width:105px;height:30px;background:var(--brand);color:#fff;font-size:11px;font-weight:700;display:flex;align-items:center;justify-content:space-between;padding:0 8px;border-bottom:2px solid var(--brand-light)}
.welcome{left:751px;top:0;width:247px;height:32px;background:#fff;color:var(--brand);font-size:11px;font-weight:700;display:flex;align-items:center;padding-left:17px;gap:0}
.welcome svg{position:absolute;top:6px}
.logo{left:178px;top:63px;width:245px;height:80px;background:#fff;display:flex;align-items:center;justify-content:center;gap:8px}
.logo .dot{width:26px;height:26px;border-radius:50%;background:var(--brand-light)}
.logo span{color:var(--brand-light);font-size:22px;font-weight:600}
.nav{left:423px;top:63px;width:495px;height:80px;background:var(--brand);display:flex}
.nav a{color:#fff;font-size:11.5px;font-weight:700;text-decoration:none;display:flex;align-items:center;justify-content:center;width:82.5px}
.nav a.home{background:var(--brand-light)}
.search{left:918px;top:63px;width:80px;height:80px;background:var(--teal-strong);display:flex;align-items:center;justify-content:center}
.finder{left:178px;top:310px;width:410px;height:507px;background:var(--panel)}
.finder h2,.login h2{position:absolute;top:20px;font-size:14.5px;font-weight:800;color:#fff}
.finder h2{left:24px}
.field-label{position:absolute;left:24px;color:#fff;font-size:14.5px}
.input{position:absolute;left:164px;width:222px;height:40px;background:#fff;font-size:12.5px;color:#b5b9c0;display:flex;align-items:center;padding-left:15px}
.input.filled{color:var(--ink);border:1px solid #1b4fb8}
.radio{position:absolute;color:#fff;font-size:14.5px;display:flex;align-items:center;gap:14px}
.radio i{width:10px;height:10px;border-radius:50%;border:2px solid #fff;display:inline-block}
.radio i.on{background:#fff}
.finder-foot{position:absolute;left:0;top:418px;width:410px;height:89px;background:var(--panel-dark)}
.btn{position:absolute;height:40px;color:#fff;font-size:13px;display:flex;align-items:center;justify-content:center;background:var(--btn-dark)}
.login{left:610px;top:310px;width:388px;height:253px;background:var(--teal)}
.login h2{left:24px}
.login .become{position:absolute;right:24px;top:20px;font-size:14.5px;font-weight:800;color:var(--navy)}
.login .field-label{left:23px}
.login .input{left:141px;width:223px;color:var(--ink);font-weight:700;font-size:13px}
.login .input svg{position:absolute;right:10px;top:8px}
.forgot{position:absolute;left:26px;top:199px;font-size:13px;color:#1e8f9a;text-decoration:underline}
.login .btn{left:247px;top:188px;width:117px;background:var(--brand)}
.perks{left:610px;top:563px;width:388px;height:254px;background:#fff;padding:14px 24px}
.perks h3{color:var(--brand);font-size:19.5px;font-weight:700;margin-bottom:10px}
.perks li{list-style:none;display:flex;align-items:center;gap:14px;height:38.5px;font-size:14.5px}
.rule{left:119px;top:857px;width:960px;height:1px;background:var(--line)}
.results-title{left:0;top:872px;width:1200px;text-align:center;font-size:25px;font-weight:800;color:var(--navy)}
.cols{top:921px;font-size:12.5px;color:var(--muted)}
.row{left:119px;width:960px;height:82px;background:#fff;display:flex}
.row>div{display:flex;align-items:center;justify-content:center;border-right:1px solid #e6e6e6;font-size:12.5px;text-align:center}
.row .name{width:139px;background:var(--navy);color:#fff;font-weight:800;font-size:12.5px;line-height:15px}
.row .spec{font-weight:600}
.row .phone{font-weight:700}
.row .go{width:38px;background:var(--teal);border-right:3px solid var(--brand)!important}
</style>
</head>
<body>
<div class="abs top-band"></div>
<div class="abs hero" role="img" aria-label="Photo of a doctor in a white coat with arms crossed and a stethoscope"></div>

<div class="abs lang">ENGLISH <svg width="9" height="8" viewBox="0 0 9 8"><path d="M1 1h7L4.5 7z" fill="none" stroke="#fff" stroke-width="1.3"/></svg></div>
<div class="abs welcome">WELCOME MAREK
  <svg style="left:186px" width="20" height="20" viewBox="0 0 20 20" fill="none" stroke="#1e5fd8" stroke-width="1.4"><circle cx="10" cy="6.5" r="4.5"/><path d="M2 19c0-4.5 3.6-7 8-7s8 2.5 8 7z"/></svg>
  <svg style="left:220px" width="18" height="20" viewBox="0 0 18 20" fill="none" stroke="#1e5fd8" stroke-width="1.4"><path d="M5 9V5a4 4 0 018 0"/><rect x="2" y="9" width="14" height="10" rx="2"/><circle cx="9" cy="14" r="1.5"/></svg>
</div>

<div class="abs logo"><i class="dot"></i><span>Dr. Lumora</span></div>
<nav class="abs nav">
  <a class="home">HOME</a><a>DOCTOR’S</a><a>HEALTH</a><a>ABOUT</a><a>NEWS</a><a>CONTACT</a>
</nav>
<div class="abs search"><svg width="28" height="28" viewBox="0 0 28 28" fill="none" stroke="#fff" stroke-width="1.5"><circle cx="12" cy="12" r="10"/><path d="M19 19l7 7"/></svg></div>

<section class="abs finder">
  <h2>FIND A DOCTOR</h2>
  <span class="field-label" style="top:55px">Doctor’s name</span>
  <div class="input filled" style="top:59px">Marek Solan|</div>
  <span class="field-label" style="top:118px">Doctor’s name</span>
  <span class="radio" style="left:165px;top:118px"><i></i>Male</span>
  <span class="radio" style="left:275px;top:118px"><i class="on"></i>Female</span>
  <span class="field-label" style="top:169px">Specialisation</span>
  <div class="input" style="top:159px">Choose specialisation</div>
  <span class="field-label" style="top:234px">Symptoms</span>
  <div class="input" style="top:224px">Choose symptoms</div>
  <span class="field-label" style="top:298px">District</span>
  <div class="input" style="top:288px">Choose district
    <svg style="position:absolute;right:16px;top:16px" width="9" height="8" viewBox="0 0 9 8"><path d="M1 1h7L4.5 7z" fill="none" stroke="#1e5fd8" stroke-width="1.3"/></svg></div>
  <span class="field-label" style="top:363px">Phone number</span>
  <div class="input" style="top:353px">Enter your phone number</div>
  <div class="finder-foot"></div>
  <div class="btn" style="left:24px;top:442px;width:116px">RESET</div>
  <div class="btn" style="left:164px;top:442px;width:222px">SEARCH DOCTOR</div>
</section>

<section class="abs login">
  <h2>MEMBER LOGIN</h2>
  <span class="become">BECOME A MEMBER</span>
  <span class="field-label" style="top:55px">Login email</span>
  <div class="input" style="top:59px">marek@studio-ms.pl
    <svg width="24" height="24" viewBox="0 0 24 24" fill="none" stroke="#6ee3dc" stroke-width="1.4"><circle cx="12" cy="12" r="11"/><path d="M7.5 12.5l3 3 6-6"/></svg></div>
  <span class="field-label" style="top:120px">Password</span>
  <div class="input" style="top:124px">************
    <svg width="24" height="24" viewBox="0 0 24 24" fill="none" stroke="#e8434b" stroke-width="1.4"><circle cx="12" cy="12" r="11"/><path d="M9 9l6 6M15 9l-6 6"/></svg></div>
  <a class="forgot">Forgot password?</a>
  <div class="btn">LOGIN</div>
</section>

<section class="abs perks">
  <h3>BECOME A DR. LUMORA MEMBER!</h3>
  <ul>
    <li><svg width="26" height="26" viewBox="0 0 26 26" fill="none" stroke="#6ee3dc" stroke-width="1.4"><circle cx="13" cy="13" r="12"/><path d="M8.5 13.5l3 3 6-6"/></svg>First hand health news</li>
    <li><svg width="26" height="26" viewBox="0 0 26 26" fill="none" stroke="#6ee3dc" stroke-width="1.4"><circle cx="13" cy="13" r="12"/><path d="M8.5 13.5l3 3 6-6"/></svg>Exclusive promotions</li>
    <li><svg width="26" height="26" viewBox="0 0 26 26" fill="none" stroke="#6ee3dc" stroke-width="1.4"><circle cx="13" cy="13" r="12"/><path d="M8.5 13.5l3 3 6-6"/></svg>Instant health advices</li>
    <li><svg width="26" height="26" viewBox="0 0 26 26" fill="none" stroke="#6ee3dc" stroke-width="1.4"><circle cx="13" cy="13" r="12"/><path d="M8.5 13.5l3 3 6-6"/></svg>Free health seminars / talks</li>
    <li><svg width="26" height="26" viewBox="0 0 26 26" fill="none" stroke="#6ee3dc" stroke-width="1.4"><circle cx="13" cy="13" r="12"/><path d="M8.5 13.5l3 3 6-6"/></svg>Priority doctor appointments</li>
  </ul>
</section>

<div class="abs rule"></div>
<h2 class="abs results-title">TOP RESOULTS</h2>
<span class="abs cols" style="left:119px">DOCTOR NAME</span>
<span class="abs cols" style="left:274px">GENDER</span>
<span class="abs cols" style="left:365px">SPECIALISATION</span>
<span class="abs cols" style="left:518px">XXX</span>
<span class="abs cols" style="left:628px">XXX</span>
<span class="abs cols" style="left:723px">ADDRESS</span>
<span class="abs cols" style="left:818px">DISTRICT</span>
<span class="abs cols" style="left:917px">PHONE NUMBER</span>

<div class="abs row" style="top:950px">
  <div class="name">MAREK<br>SOLAN</div>
  <div style="width:83px"><svg width="26" height="26" viewBox="0 0 26 26" fill="none" stroke="#1a4fb8" stroke-width="3.5"><circle cx="10" cy="16" r="7"/><path d="M15 11l8-8M16 3h7v7"/></svg></div>
  <div class="spec" style="width:148px">Graphic Designer</div>
  <div style="width:81px">Private</div>
  <div style="width:140px">marek@studio-ms.pl</div>
  <div style="width:81px"><svg width="20" height="26" viewBox="0 0 20 26" fill="none" stroke="#1e5fd8" stroke-width="1.5"><path d="M10 25S2 15 2 9.5a8 8 0 0116 0C18 15 10 25 10 25z"/><circle cx="10" cy="9.5" r="2.5"/></svg></div>
  <div style="width:108px">District</div>
  <div class="phone" style="width:139px">+44 700481522</div>
  <div class="go"><svg width="28" height="28" viewBox="0 0 28 28" fill="none" stroke="#1e5fd8" stroke-width="1.5"><path d="M11 5h13v18H11M2 14h14M12 10l4 4-4 4"/></svg></div>
</div>
<div class="abs row" style="top:1040px">
  <div class="name">MAREK<br>SOLAN</div>
  <div style="width:83px"><svg width="26" height="26" viewBox="0 0 26 26" fill="none" stroke="#1a4fb8" stroke-width="3.5"><circle cx="10" cy="16" r="7"/><path d="M15 11l8-8M16 3h7v7"/></svg></div>
  <div class="spec" style="width:148px">Graphic Designer</div>
  <div style="width:81px">Private</div>
  <div style="width:140px">XXX</div>
  <div style="width:81px"><svg width="20" height="26" viewBox="0 0 20 26" fill="none" stroke="#1e5fd8" stroke-width="1.5"><path d="M10 25S2 15 2 9.5a8 8 0 0116 0C18 15 10 25 10 25z"/><circle cx="10" cy="9.5" r="2.5"/></svg></div>
  <div style="width:108px">District</div>
  <div class="phone" style="width:139px">+44 700481522</div>
  <div class="go"><svg width="28" height="28" viewBox="0 0 28 28" fill="none" stroke="#1e5fd8" stroke-width="1.5"><path d="M11 5h13v18H11M2 14h14M12 10l4 4-4 4"/></svg></div>
</div>
<div class="abs row" style="top:1130px">
  <div class="name">MAREK<br>SOLAN</div>
  <div style="width:83px"><svg width="26" height="26" viewBox="0 0 26 26" fill="none" stroke="#1a4fb8" stroke-width="3.5"><circle cx="10" cy="16" r="7"/><path d="M15 11l8-8M16 3h7v7"/></svg></div>
  <div class="spec" style="width:148px">Graphic Designer</div>
  <div style="width:81px">Private</div>
  <div style="width:140px">XXX</div>
  <div style="width:81px"><svg width="20" height="26" viewBox="0 0 20 26" fill="none" stroke="#1e5fd8" stroke-width="1.5"><path d="M10 25S2 15 2 9.5a8 8 0 0116 0C18 15 10 25 10 25z"/><circle cx="10" cy="9.5" r="2.5"/></svg></div>
  <div style="width:108px">District</div>
  <div class="phone" style="width:139px">+44 700481522</div>
  <div class="go"><svg width="28" height="28" viewBox="0 0 28 28" fill="none" stroke="#1e5fd8" stroke-width="1.5"><path d="M11 5h13v18H11M2 14h14M12 10l4 4-4 4"/></svg></div>
</div>
</body>
</html>
```